BRQL project
Cloudward Trainer Bench Systems
i dont see, button or anything ,,,...
about handover...anyone help me..??
i am first in here..how way the rule and upload my file to ch....
The project has been extended for 3 more days.
Ruth.
Hi,
I want only static
hello ! my name is Ida :) I want to participate this nice contest ~! Haven't one .ai format logo ? I not understand static or animated banner !? please more details - thanks
or not of*
flash of animated gif?
I would like to see it animated also
Do you need it animated?
I would like to see also a new with the wgt lifter text to be replaced by Vortek WGT PC.
Also add the bellow text
Increase WGT performance by 30% and more
It would be great if you could give specific text content / copy. Please mention your preferred colors and other specifications(if any). A more detailed design brief would help.

```html
<!DOCTYPE html>
<html lang="en">
<head>
<meta charset="utf-8">
<title>Vortek WGT PC — banner set</title>
<link rel="stylesheet" href="https://fonts.googleapis.com/css2?family=Roboto+Condensed:wght@700&family=Arimo:wght@700&display=swap">
<style>
  :root {
    --stage: #000000;
    --sky-light: #f2c15a;
    --sky-mid: #c9772a;
    --sky-dark: #4a2a14;
    --gold: #f4b82a;
    --blue-top: #1057c0;
    --blue-bottom: #062e86;
    --orange: #f7941d;
    --white: #ffffff;
    --silver: #e4e6ea;
    --badge-ring: #9aa3ad;
  }
  * { margin: 0; padding: 0; box-sizing: border-box; }
  html, body { width: 1200px; height: 845px; overflow: hidden; background: var(--stage); }
  .canvas { position: relative; width: 1200px; height: 845px; }
  .banner { position: absolute; overflow: hidden; }
  .banner svg.backdrop { position: absolute; inset: 0; }
  .banner-leaderboard { left: 271px; top: 48px; width: 886px; height: 110px; }
  .banner-square { left: 271px; top: 175px; width: 365px; height: 305px; }
  .banner-skyscraper { left: 60px; top: 48px; width: 197px; height: 732px; }

  .title {
    position: absolute;
    font-family: "Roboto Condensed", sans-serif;
    font-weight: 700;
    color: var(--silver);
    line-height: 0.95;
    letter-spacing: 1px;
    text-shadow: 0 2px 3px rgba(0,0,0,0.55);
  }
  .copy {
    position: absolute;
    font-family: "Arimo", sans-serif;
    font-weight: 700;
    color: var(--white);
    line-height: 1.05;
  }
  .accent { color: var(--orange); }

  .banner-leaderboard .title { left: 22px; top: 10px; font-size: 42px; }
  .banner-leaderboard .copy { left: 628px; top: 14px; }
  .banner-leaderboard .copy .headline { font-size: 29px; }
  .banner-leaderboard .copy .sub { font-size: 23px; }
  .banner-leaderboard .copy .small { font-size: 19px; }

  .banner-square .title { left: 18px; top: 10px; font-size: 42px; }
  .banner-square .copy { left: 10px; top: 237px; }
  .banner-square .copy .headline { font-size: 29px; }
  .banner-square .copy .sub { font-size: 21px; }
  .banner-square .copy .small { font-size: 17px; }

  .banner-skyscraper .title { left: 0; width: 197px; top: 410px; font-size: 50px; text-align: center; color: var(--white); }
  .banner-skyscraper .copy { left: 0; width: 197px; top: 530px; text-align: center; }
  .banner-skyscraper .copy .headline { font-size: 25px; }
  .banner-skyscraper .copy .sub { font-size: 22px; }
  .banner-skyscraper .copy .big { font-size: 40px; margin-top: 16px; display: block; }
  .banner-skyscraper .copy .big .num { font-size: 46px; }
  .banner-skyscraper .copy .more { font-size: 32px; display: block; }
</style>
</head>
<body>
<main class="canvas">

  <section class="banner banner-leaderboard">
    <svg class="backdrop" width="886" height="110" viewBox="0 0 886 110">
      <defs>
        <linearGradient id="sky-wide" x1="0" y1="0" x2="1" y2="1">
          <stop offset="0" stop-color="var(--sky-dark)"/>
          <stop offset="0.45" stop-color="var(--sky-light)"/>
          <stop offset="1" stop-color="var(--sky-mid)"/>
        </linearGradient>
        <linearGradient id="blue-wide" x1="0" y1="0" x2="0" y2="1">
          <stop offset="0" stop-color="var(--blue-top)"/>
          <stop offset="1" stop-color="var(--blue-bottom)"/>
        </linearGradient>
      </defs>
      <rect width="640" height="110" fill="url(#sky-wide)" role="img" aria-label="Photo of a passenger jet climbing through a golden sunset sky"/>
      <path d="M596,0 Q576,55 602,110 L886,110 L886,0 Z" fill="var(--gold)"/>
      <path d="M606,0 Q588,55 612,110 L886,110 L886,0 Z" fill="url(#blue-wide)"/>
      <circle class="badge" cx="574" cy="48" r="38" fill="var(--white)" stroke="var(--badge-ring)" stroke-width="5"/>
    </svg>
    <h2 class="title">VORTEK<br>WGT PC</h2>
    <p class="copy">
      <span class="headline accent">INCREASE WGT</span><br>
      <span class="sub">PERFORMANCE</span><br>
      <span class="small">by <span class="accent">30%</span> and more!</span>
    </p>
  </section>

  <section class="banner banner-square">
    <svg class="backdrop" width="365" height="305" viewBox="0 0 365 305">
      <defs>
        <linearGradient id="sky-square" x1="0" y1="0" x2="1" y2="1">
          <stop offset="0" stop-color="var(--sky-dark)"/>
          <stop offset="0.5" stop-color="var(--sky-light)"/>
          <stop offset="1" stop-color="var(--sky-mid)"/>
        </linearGradient>
        <linearGradient id="blue-square" x1="0" y1="0" x2="0" y2="1">
          <stop offset="0" stop-color="var(--blue-top)"/>
          <stop offset="1" stop-color="var(--blue-bottom)"/>
        </linearGradient>
      </defs>
      <rect width="365" height="260" fill="url(#sky-square)" role="img" aria-label="Photo of a passenger jet flying above clouds at sunset"/>
      <path d="M0,222 Q190,190 365,150 L365,305 L0,305 Z" fill="var(--gold)"/>
      <path d="M0,234 Q190,205 365,168 L365,305 L0,305 Z" fill="url(#blue-square)"/>
      <circle class="badge" cx="305" cy="209" r="36" fill="var(--white)" stroke="var(--badge-ring)" stroke-width="5"/>
    </svg>
    <h2 class="title">VORTEK WGT PC</h2>
    <p class="copy">
      <span class="headline accent">INCREASE WGT</span><br>
      <span class="sub">PERFORMANCE</span> <span class="small">by <span class="accent">30%</span> and more!</span>
    </p>
  </section>

  <section class="banner banner-skyscraper">
    <svg class="backdrop" width="197" height="732" viewBox="0 0 197 732">
      <defs>
        <linearGradient id="sky-tall" x1="0" y1="0" x2="1" y2="1">
          <stop offset="0" stop-color="var(--sky-mid)"/>
          <stop offset="0.45" stop-color="var(--sky-light)"/>
          <stop offset="1" stop-color="var(--sky-dark)"/>
        </linearGradient>
        <linearGradient id="blue-tall" x1="0" y1="0" x2="0" y2="1">
          <stop offset="0" stop-color="var(--blue-top)"/>
          <stop offset="1" stop-color="var(--blue-bottom)"/>
        </linearGradient>
      </defs>
      <rect width="197" height="380" fill="url(#sky-tall)" role="img" aria-label="Photo of a passenger jet in a sunset sky"/>
      <path d="M0,318 Q110,368 197,292 L197,732 L0,732 Z" fill="var(--gold)"/>
      <path d="M0,336 Q110,386 197,312 L197,732 L0,732 Z" fill="url(#blue-tall)"/>
      <circle class="badge" cx="161" cy="312" r="36" fill="var(--white)" stroke="var(--badge-ring)" stroke-width="5"/>
    </svg>
    <h2 class="title">VORTEK<br>WGT PC</h2>
    <p class="copy">
      <span class="headline accent">INCREASE WGT</span><br>
      <span class="sub accent">PERFORMANCE</span>
      <span class="big">by <span class="num accent">30%</span></span>
      <span class="more">and more!</span>
    </p>
  </section>

</main>
</body>
</html>
```